Modern Innovative Business Card Design

We require a nice, modern, clean business card design, ready for upload to Cardomora. Our company develops online banking software solutions for small financial insitutions. The design should be clean, professional, but yet not "corporate boring". See www.fyrolt.com for an idea of business image and profile. The design should communicate innovation, be modern and fresh, yet look professional and established.

Target Market(s)

Finance industry, bankers, entrepreneurs

Industry/Entity Type

Financial

Contact Information for Business Card

Tobias Wendlerup
CEO

FYROLT BV
Lindenwerf 38
1027 HX Amsterdam
The Netherlands

Phone: +31 20 517 8036
Direct: +31 20 604 1758
Skype: tobias.fyrolt
ceo@fyrolt.com
www.fyrolt.com

Font styles to use
Sans Serif

Requirements
Must have
• Should look clean, modern and professional. File should be ready for upload to cardomora.
Should not have
• Boring standard corporate layout

```html
<!DOCTYPE html>
<html lang="en">
<head>
<meta charset="utf-8">
<title>FYROLT – Business Card</title>
<link href="https://fonts.googleapis.com/css2?family=Questrial&family=Montserrat:wght@700&display=swap" rel="stylesheet">
<style>
  :root {
    --stage: #e6e6e4;
    --card-dark: #3c3c3c;
    --card-dark-deep: #333333;
    --card-light: #ffffff;
    --accent: #8cc21f;
    --text-light: #e4e4e4;
    --text-muted: #cfcfcf;
    --text-dark: #3a3a3a;
  }
  * { box-sizing: border-box; margin: 0; padding: 0; }
  html, body { width: 1200px; height: 871px; overflow: hidden; }
  body {
    position: relative;
    background: var(--stage);
    font-family: "Questrial", "Century Gothic", sans-serif;
  }
  .card {
    position: absolute;
    width: 540px;
    height: 309px;
    border-radius: 3px;
    overflow: hidden;
    box-shadow: 0 10px 28px rgba(0,0,0,.22);
  }

  /* Back of card */
  .card--back {
    left: 60px; top: 100px;
    background: linear-gradient(160deg, var(--card-dark) 0%, var(--card-dark-deep) 100%);
  }
  .card--back .brand-name {
    position: absolute;
    left: 132px; top: 82px;
    font-size: 68px;
    letter-spacing: 3px;
    color: var(--text-light);
  }
  .card--back .accent-band {
    position: absolute;
    left: 0; right: 0; top: 196px;
    height: 40px;
    background: var(--accent);
    display: flex;
    align-items: center;
    justify-content: center;
    gap: 48px;
  }
  .band-item {
    display: flex;
    align-items: center;
    gap: 10px;
    font-size: 15px;
    letter-spacing: .5px;
    color: var(--text-dark);
  }
  .band-item svg { width: 18px; height: 18px; }

  /* Front of card */
  .card--front {
    left: 600px; top: 462px;
    background: var(--card-light);
  }
  .card--front .brand-name {
    position: absolute;
    left: 34px; top: 30px;
    font-size: 40px;
    letter-spacing: 2px;
    color: var(--text-dark);
  }
  .card--front .info-band {
    position: absolute;
    left: 0; right: 0; top: 106px;
    height: 172px;
    background: var(--card-dark);
  }
  .person {
    position: absolute;
    left: 34px; top: 24px;
  }
  .person__name {
    font-family: "Montserrat", "Century Gothic", sans-serif;
    font-weight: 700;
    font-size: 16px;
    letter-spacing: .5px;
    color: #ffffff;
  }
  .person__role {
    margin-top: 4px;
    font-size: 13px;
    color: var(--accent);
  }
  .company {
    position: absolute;
    left: 290px; top: 20px;
    font-size: 12.5px;
    line-height: 1.5;
    letter-spacing: .5px;
    color: var(--text-muted);
  }
  .contact-list {
    list-style: none;
    margin-top: 10px;
  }
  .contact-list li {
    display: flex;
    align-items: center;
    gap: 12px;
    line-height: 1.55;
  }
  .contact-list svg { width: 13px; height: 13px; flex: none; }
</style>
</head>
<body>

  <section class="card card--back" aria-label="Business card back">
    <div class="brand-name">FYROLT</div>
    <div class="accent-band">
      <span class="band-item">
        <svg viewBox="0 0 20 20" aria-hidden="true">
          <circle cx="10" cy="10" r="8" fill="none" stroke="#ffffff" stroke-width="1.6"/>
          <ellipse cx="10" cy="10" rx="3.5" ry="8" fill="none" stroke="#ffffff" stroke-width="1.4"/>
          <line x1="2" y1="10" x2="18" y2="10" stroke="#ffffff" stroke-width="1.4"/>
        </svg>
        www.fyrolt.com
      </span>
      <span class="band-item">
        <svg viewBox="0 0 20 20" aria-hidden="true">
          <circle cx="10" cy="10" r="9" fill="#ffffff"/>
        </svg>
        tobias.fyrolt
      </span>
    </div>
  </section>

  <section class="card card--front" aria-label="Business card front">
    <div class="brand-name">FYROLT</div>
    <div class="info-band">
      <div class="person">
        <div class="person__name">Tobias Wendlerup</div>
        <div class="person__role">CEO</div>
      </div>
      <div class="company">
        <div>FYROLT BV</div>
        <div>Lindenwerf 38 1027 HX</div>
        <div>Amsterdam The Netherlands</div>
        <ul class="contact-list">
          <li>
            <svg viewBox="0 0 16 16" aria-hidden="true">
              <path d="M2 6 Q8 1 14 6 L12 8 L10 6.5 L6 6.5 L4 8 Z" fill="none" stroke="#8cc21f" stroke-width="1.3" stroke-linejoin="round"/>
              <rect x="4" y="9" width="8" height="5" rx="1" fill="none" stroke="#8cc21f" stroke-width="1.3"/>
            </svg>
            +31 20 517 8036
          </li>
          <li>
            <svg viewBox="0 0 16 16" aria-hidden="true">
              <path d="M2 6 Q8 1 14 6 L12 8 L10 6.5 L6 6.5 L4 8 Z" fill="none" stroke="#8cc21f" stroke-width="1.3" stroke-linejoin="round"/>
              <rect x="4" y="9" width="8" height="5" rx="1" fill="none" stroke="#8cc21f" stroke-width="1.3"/>
            </svg>
            +31 20 604 1758
          </li>
          <li>
            <svg viewBox="0 0 16 16" aria-hidden="true">
              <rect x="1.5" y="3.5" width="13" height="9" fill="none" stroke="#8cc21f" stroke-width="1.3"/>
              <polyline points="1.5,3.5 8,9 14.5,3.5" fill="none" stroke="#8cc21f" stroke-width="1.3"/>
            </svg>
            ceo@fyrolt.com
          </li>
        </ul>
      </div>
    </div>
  </section>

</body>
</html>
```